Business Card Design Project - KLB

I am looking for a more sophisticated card design for my company,
"The Kestrel Bureau"

We are a consultancy focused on strategy and change in Associations and professional organisations.

I am a lawyer and psychologist with a PhD and so am looking for something that communicates seriousness and credibility but also quirky creative solutions for strategic problems, which is my field of speciality.

I am looking for something that is quietly spoken, rather than loud colours ('credible' and 'creative' are the two adjectives that I think of as competing here).

I particularly like an embossed card style - heavy white card with plain white or white and black or white and grey text.

The key logo image for the company is a question mark and I am open to suggestions and ideas on design.

I have attached a file that includes a couple of styles that have caught my eye and my thoughts on them. Hopefully they communicate what I'm looking for.
Updates

Thank you for all the great suggestions and designs.

I really appreciated the effort and creative energy you put into your designs. I have now closed the project after selecting a design and advising the successful designer of the card that I am happy with.

Regards

Target Market(s)

Organisations (CEO's and Boards), Governments, Legal professionals, Membership Associations and aspiring professionals.

Industry/Entity Type

Lawyer

Requirements
Must have
• The key logo element is a question mark (?) and this needs to be incorporated.

Embossed style - cut outs or other design ideas interest me too.

The attached file has a number of sample ideas and comments on each one that I like.
Should not have
• I like crisp, modern fonts (Myriads etc...) and do not like embellished fonts or Times etc...

```html
<!DOCTYPE html>
<html lang="en">
<head>
<meta charset="utf-8">
<title>The Kestrel Bureau — Business Card</title>
<link rel="stylesheet" href="https://fonts.googleapis.com/css2?family=Source+Sans+3:wght@400;600&display=swap">
<style>
  :root {
    --backdrop: #e9e7e4;
    --card-stock: #fbfbfa;
    --card-edge: #d9d8d5;
    --ink: #141414;
    --emboss-mark: #e6e6e4;
  }
  html, body {
    margin: 0;
    padding: 0;
    width: 1200px;
    height: 799px;
    overflow: hidden;
    background: var(--backdrop);
  }
  .canvas {
    position: relative;
    width: 1200px;
    height: 799px;
    display: flex;
    align-items: center;
    justify-content: center;
  }
  .business-card {
    position: relative;
    width: 770px;
    height: 440px;
    background: var(--card-stock);
    border: 1px solid var(--card-edge);
    box-shadow: 0 6px 18px rgba(0, 0, 0, 0.12);
    font-family: "Source Sans 3", sans-serif;
    color: var(--ink);
    overflow: hidden;
  }
  .emboss-mark {
    position: absolute;
    left: 60px;
    top: 110px;
    width: 300px;
    height: 300px;
  }
  .company-name {
    position: absolute;
    left: 28px;
    top: 34px;
    margin: 0;
    font-size: 48px;
    font-weight: 400;
    letter-spacing: -0.5px;
    line-height: 1;
  }
  .person {
    position: absolute;
    left: 262px;
    top: 150px;
  }
  .person-name {
    margin: 0 0 8px;
    font-size: 32px;
    font-weight: 400;
    line-height: 1;
  }
  .person-title,
  .tagline {
    margin: 0 0 6px;
    font-size: 22px;
    font-weight: 400;
    line-height: 1.1;
  }
  .contact {
    position: absolute;
    left: 462px;
    top: 318px;
    font-size: 15px;
    line-height: 1.9;
    letter-spacing: -0.2px;
  }
  .contact p { margin: 0; }
</style>
</head>
<body>
  <main class="canvas">
    <article class="business-card">
      <svg class="emboss-mark" viewBox="0 0 300 300" aria-hidden="true">
        <circle cx="150" cy="150" r="140" fill="var(--emboss-mark)"/>
      </svg>

      <h1 class="company-name">The Kestrel Bureau</h1>

      <section class="person">
        <p class="person-name">Daniel Hartley</p>
        <p class="person-title">Vice President of Marketing</p>
        <p class="tagline">Let Us Show You Why</p>
      </section>

      <address class="contact">
        <p>48 Alder Row Fenwick, Vale County</p>
        <p>Phone 800-555-0193</p>
      </address>
    </article>
  </main>
</body>
</html>
```